Elk Ridge Baptist Church sign

We want a colourful, attractive sign that includes connection to being a Christian Church living in the foothills of the Canadian Rocky Mountains. As far as printed words, we need it to say “ Elk Ridge Baptist Church”. We are planning on a sign that is 6’ x 4’. Our church slogan is:
“ Live like Jesus, Love like Jesus”. This slogan could be included on the sign if space allows. To all designers; in talking with the communications team at our church, we want to eliminate the church’s slogan “ live like Jesus, live like Jesus “, from being on the sign.

```html
<!DOCTYPE html>
<html lang="en">
<head>
<meta charset="utf-8">
<title>Elk Ridge Baptist Church – Sign</title>
<link rel="stylesheet" href="https://fonts.googleapis.com/css2?family=Allura&family=Libre+Caslon+Text:wght@400;700&display=swap">
<style>
  :root {
    --backdrop: #7a7a7a;
    --sign-blue: #0b4ca8;
    --wave-navy: #1d2f7a;
    --wave-sky: #19a2e6;
    --wave-white: #ffffff;
    --text-white: #ffffff;
    --script-shadow: #7cb9ec;
    --photo-sky: #8cc4e4;
    --photo-hills: #3f8a9a;
    --photo-forest: #2c6a3c;
  }
  html, body {
    margin: 0;
    padding: 0;
    width: 889px;
    height: 1200px;
    overflow: hidden;
    background: var(--backdrop);
  }
  .canvas {
    position: relative;
    width: 889px;
    height: 1200px;
  }
  .sign {
    position: absolute;
    left: 30px;
    top: 323px;
    width: 829px;
    height: 553px;
    box-shadow: 0 4px 10px rgba(0,0,0,0.35);
  }
  .sign svg {
    display: block;
    width: 100%;
    height: 100%;
  }
  .sign-eyebrow {
    font-family: "Libre Caslon Text", "Times New Roman", serif;
    font-weight: 700;
    font-size: 42px;
    letter-spacing: 1px;
    fill: var(--text-white);
  }
  .sign-name {
    font-family: "Allura", cursive;
    font-size: 200px;
    fill: var(--text-white);
    filter: drop-shadow(4px 3px 0 var(--script-shadow));
  }
</style>
</head>
<body>
<main class="canvas">
  <section class="sign">
    <svg viewBox="0 0 876 585" xmlns="http://www.w3.org/2000/svg">
      <defs>
        <linearGradient id="landscapeTones" x1="0" y1="0" x2="0" y2="1">
          <stop offset="0" stop-color="var(--photo-sky)"/>
          <stop offset="0.3" stop-color="var(--photo-hills)"/>
          <stop offset="0.6" stop-color="var(--photo-forest)"/>
        </linearGradient>
        <linearGradient id="waveHighlight" x1="0" y1="0" x2="1" y2="0">
          <stop offset="0" stop-color="var(--wave-sky)"/>
          <stop offset="0.3" stop-color="var(--wave-white)"/>
          <stop offset="0.6" stop-color="var(--wave-sky)"/>
          <stop offset="1" stop-color="var(--wave-sky)"/>
        </linearGradient>
        <path id="eyebrowArc" d="M58,398 Q230,318 420,375"/>
      </defs>

      <rect class="sign-landscape" role="img" aria-label="Photograph of the Rocky Mountain foothills with snowy peaks, green fields and forest"
            x="0" y="0" width="876" height="585" fill="url(#landscapeTones)"/>

      <path class="wave-sky" d="M0,255 C180,170 330,262 500,308 C650,348 790,262 876,190 L876,585 L0,585Z" fill="var(--wave-sky)"/>
      <path class="wave-highlight" d="M0,272 C180,192 330,278 500,322 C650,360 790,276 876,206 L876,585 L0,585Z" fill="url(#waveHighlight)"/>
      <path class="wave-navy" d="M0,290 C180,212 330,292 500,334 C650,370 790,288 876,220 L876,585 L0,585Z" fill="var(--wave-navy)"/>
      <path class="wave-line" d="M0,306 C180,228 330,304 500,345 C650,380 790,300 876,233 L876,585 L0,585Z" fill="var(--wave-white)"/>
      <path class="sign-field" d="M0,310 C180,232 330,308 500,349 C650,384 790,304 876,237 L876,585 L0,585Z" fill="var(--sign-blue)"/>

      <rect class="church-sketch" role="img" aria-label="Faint line drawing of a church building"
            x="640" y="340" width="220" height="240" fill="#ffffff" opacity="0.025"/>

      <text class="sign-eyebrow"><textPath href="#eyebrowArc">ELK RIDGE</textPath></text>
      <text class="sign-name" x="52" y="515" textLength="750" lengthAdjust="spacingAndGlyphs">Baptist Church</text>
    </svg>
  </section>
</main>
</body>
</html>
```